Accountability Project Graphics

I want to create 10 social media graphics (new Instagram size 4:5 (1080 x 1350 pixels) focusing on our Kelmora Accountability App, using any of the 3 pictures attached. Use the attached pics only, NO RANDOM STOCK PHOTOGRAPHY. For the color scheme, use the landing page colors/fonts (attached).
You can add any of the 3 photos attached but I mainly need BOLD text that includes these headlines and sub-headlines on them.
Please NOTE for all the headlines below, also add this sub-headline on each graphic:
Stay Consistent with MB in Your Pocket!
Here are the headlines:
• Stop Starting Over Every Monday
• You don't need more willpower. You need more support
• Built for women who are tired of doing this alone
• When Motivation Fades, MB Checks In
• The Support System You've Been Missing
• Support When Motivation Disappears
• What if MB Checked in Every Day?
• The Missing Piece Isn't Another Diet
• Eat the food you love. Stay accountable every day.
• One Bad Meal Doesn't Mean You Failed
women over 40 trying to lose weight

```html
<!DOCTYPE html>
<html lang="en">
<head>
<meta charset="utf-8">
<title>Kelmora Accountability App – Social Graphics</title>
<link href="https://fonts.googleapis.com/css2?family=Noto+Serif:ital,wght@0,700;0,800;1,700&display=swap" rel="stylesheet">
<style>
  :root{
    --stage:#707072;
    --blush:#fbe1e8;
    --white:#ffffff;
    --plum:#2d1240;
    --plum-deep:#341743;
    --plum-soft:#4a2a5c;
    --rose:#d6467f;
    --photo-light:#e9c9d4;
    --photo-dark:#2a2533;
  }
  *{margin:0;padding:0;box-sizing:border-box}
  html,body{width:1200px;height:1115px;overflow:hidden;background:var(--stage)}
  body{position:relative;font-family:"Noto Serif",Georgia,serif}
  .post{position:absolute;width:284px;height:354px;overflow:hidden;
    background:linear-gradient(180deg,var(--blush) 0%,var(--blush) 70%,var(--white) 100%)}
  .arch{position:absolute;background:var(--white);border-radius:110px 110px 0 0;opacity:.85}
  .photo{position:absolute;border-radius:40px 40px 0 0}
  .photo--portrait{background:linear-gradient(180deg,var(--photo-light) 0%,var(--photo-dark) 35%,var(--photo-dark) 100%)}
  .photo--hug{background:linear-gradient(160deg,#3a2a4a 0%,#d6a37f 35%,#d94f8e 70%,#2a2533 100%)}
  .photo--duo{background:linear-gradient(180deg,#3d2c2c 0%,#b57d5e 25%,#3c5378 60%,#e8e8ee 100%)}
  .photo--lounge{background:linear-gradient(180deg,#b9a38f 0%,#6d4a3e 40%,#2a2533 100%);border-radius:0}
  .headline{position:absolute;inset:0;margin:0;font-size:0}
  .line{position:absolute;display:block;font-weight:800;line-height:1;white-space:nowrap;color:var(--plum);text-transform:uppercase}
  .line--center{left:0;width:284px;text-align:center}
  .pink{color:var(--rose)}
  .light{color:var(--white)}
  .tag{position:absolute;font-style:italic;font-weight:700;font-size:11px;line-height:1.25;color:var(--white);padding:6px 10px;border-radius:5px;white-space:nowrap}
  .tag--plum{background:linear-gradient(90deg,var(--plum) 0%,var(--plum) 55%,rgba(45,18,64,0) 100%)}
  .tag--rose{background:linear-gradient(90deg,var(--rose) 0%,var(--rose) 55%,rgba(214,70,127,0) 100%)}
  .tag--solid{background:var(--plum)}
  .post--dark{background:var(--plum-deep)}
  .post--dark .arch{background:var(--plum-soft);opacity:.5}
</style>
</head>
<body>

<!-- Row 1 -->
<section class="post" style="left:13px;top:11px">
  <div class="arch" style="left:10px;top:60px;width:240px;height:300px"></div>
  <div class="photo photo--hug" role="img" aria-label="Photo of MB hugging a smiling client" style="left:126px;top:158px;width:158px;height:196px"></div>
  <h2 class="headline">
    <span class="line" style="left:19px;top:17px;font-size:64px">When</span>
    <span class="line" style="left:19px;top:81px;font-size:32px">Motivation</span>
    <span class="line" style="left:19px;top:114px;font-size:49px">Fades,</span>
    <span class="line pink" style="left:19px;top:165px;font-size:96px">MB</span>
    <span class="line pink" style="left:19px;top:268px;font-size:29px">Checks In</span>
  </h2>
  <p class="tag tag--plum" style="left:0;top:303px;width:200px;padding-left:19px">Stay Consistent with MB<br>in Your Pocket!</p>
</section>

<section class="post" style="left:310px;top:11px">
  <div class="arch" style="left:20px;top:34px;width:200px;height:330px"></div>
  <div class="photo photo--portrait" role="img" aria-label="Photo of MB smiling with hand on hip" style="left:161px;top:86px;width:123px;height:268px"></div>
  <h2 class="headline">
    <span class="line pink" style="left:19px;top:27px;font-size:67px">Stop</span>
    <span class="line pink" style="left:19px;top:93px;font-size:30px">Starting</span>
    <span class="line pink" style="left:19px;top:122px;font-size:53px">Over</span>
    <span class="line" style="left:19px;top:171px;font-size:44px">Every</span>
    <span class="line" style="left:19px;top:209px;font-size:33px">Monday</span>
  </h2>
  <p class="tag tag--plum" style="left:19px;top:248px;width:160px">Stay Consistent with MB<br>in Your Pocket!</p>
</section>

<section class="post" style="left:606px;top:11px">
  <div class="arch" style="left:40px;top:60px;width:230px;height:300px"></div>
  <div class="photo photo--duo" role="img" aria-label="Photo of MB laughing with a friend" style="left:4px;top:161px;width:163px;height:193px"></div>
  <h2 class="headline">
    <span class="line" style="right:17px;top:23px;font-size:27px">You Don't Need</span>
    <span class="line" style="right:17px;top:49px;font-size:63px">More</span>
    <span class="line" style="right:17px;top:112px;font-size:32px">Willpower.</span>
    <span class="line pink" style="right:17px;top:146px;font-size:37px">You Need</span>
    <span class="line pink" style="right:17px;top:181px;font-size:38px">More</span>
    <span class="line pink" style="right:17px;top:221px;font-size:32px">Support</span>
  </h2>
  <p class="tag tag--rose" style="left:115px;top:259px;width:169px">Stay Consistent with MB<br>in Your Pocket!</p>
</section>

<section class="post" style="left:903px;top:11px">
  <div class="photo photo--lounge" role="img" aria-label="Photo of MB standing in a lounge with a pool table" style="left:110px;top:0;width:174px;height:354px;-webkit-mask-image:linear-gradient(90deg,transparent 0,#000 40%);mask-image:linear-gradient(90deg,transparent 0,#000 40%)"></div>
  <h2 class="headline">
    <span class="line pink" style="left:19px;top:18px;font-size:35px">Built</span>
    <span class="line pink" style="left:19px;top:52px;font-size:53px">For</span>
    <span class="line pink" style="left:19px;top:105px;font-size:27px">Women</span>
    <span class="line" style="left:19px;top:136px;font-size:22px">Who Are</span>
    <span class="line" style="left:19px;top:160px;font-size:23px">Tired Of</span>
    <span class="line" style="left:19px;top:185px;font-size:33px">Doing</span>
    <span class="line" style="left:19px;top:216px;font-size:47px">This</span>
    <span class="line" style="left:19px;top:265px;font-size:32px">Alone</span>
  </h2>
  <p class="tag tag--solid" style="left:0;top:304px;padding:5px 10px 5px 22px;font-size:10px">Stay Consistent with MB<br>in Your Pocket!</p>
</section>

<!-- Row 2 -->
<section class="post" style="left:13px;top:383px">
  <div class="arch" style="left:39px;top:21px;width:206px;height:340px"></div>
  <div class="photo photo--hug" role="img" aria-label="Photo of MB hugging a smiling client" style="left:60px;top:21px;width:160px;height:193px"></div>
  <h2 class="headline">
    <span class="line line--center pink" style="top:215px;font-size:27px">Support When</span>
    <span class="line line--center" style="top:242px;font-size:33px">Motivation</span>
    <span class="line line--center" style="top:273px;font-size:34px">Disappears</span>
  </h2>
  <p class="tag tag--solid" style="left:27px;top:312px;width:229px;padding:3px 4px;font-size:10.5px;text-align:center">Stay Consistent with MB in Your Pocket!</p>
</section>

<section class="post" style="left:310px;top:383px">
  <div class="arch" style="left:40px;top:70px;width:220px;height:300px"></div>
  <div class="photo photo--portrait" role="img" aria-label="Photo of MB smiling with hand on hip" style="left:10px;top:136px;width:148px;height:218px"></div>
  <h2 class="headline">
    <span class="line" style="right:20px;top:26px;font-size:33px">The Support</span>
    <span class="line" style="right:20px;top:57px;font-size:51px">System</span>
    <span class="line pink" style="right:20px;top:106px;font-size:45px">You've</span>
    <span class="line pink" style="right:20px;top:148px;font-size:49px">Been</span>
    <span class="line pink" style="right:20px;top:195px;font-size:33px">Missing</span>
  </h2>
  <p class="tag tag--rose" style="left:113px;top:233px;width:171px">Stay Consistent with MB<br>in Your Pocket!</p>
</section>

<section class="post" style="left:606px;top:383px">
  <div class="arch" style="left:70px;top:70px;width:180px;height:300px"></div>
  <div class="photo photo--duo" role="img" aria-label="Photo of MB laughing with a friend" style="left:127px;top:169px;width:157px;height:185px"></div>
  <h2 class="headline">
    <span class="line" style="left:22px;top:15px;font-size:49px">One Bad</span>
    <span class="line" style="left:22px;top:59px;font-size:62px">Meal</span>
    <span class="line" style="left:22px;top:117px;font-size:48px">Doesn't</span>
    <span class="line pink" style="left:22px;top:165px;font-size:36px">Mean</span>
    <span class="line pink" style="left:22px;top:200px;font-size:51px">You</span>
    <span class="line pink" style="left:22px;top:248px;font-size:37px">Failed</span>
  </h2>
  <p class="tag tag--rose" style="left:0;top:295px;width:165px;padding-left:22px">Stay Consistent with MB<br>in Your Pocket!</p>
</section>

<section class="post" style="left:903px;top:383px">
  <div class="photo photo--lounge" role="img" aria-label="Photo of MB standing in a lounge with a pool table" style="left:0;top:0;width:175px;height:354px;-webkit-mask-image:linear-gradient(90deg,#000 60%,transparent 100%);mask-image:linear-gradient(90deg,#000 60%,transparent 100%)"></div>
  <h2 class="headline">
    <span class="line" style="left:141px;width:130px;text-align:center;top:28px;font-size:23px">What If</span>
    <span class="line" style="left:131px;width:150px;text-align:center;top:45px;font-size:82px">MB</span>
    <span class="line" style="left:141px;width:130px;text-align:center;top:131px;font-size:21px">Checked</span>
    <span class="line pink" style="left:141px;width:130px;text-align:center;top:152px;font-size:66px">In</span>
    <span class="line pink" style="left:141px;width:130px;text-align:center;top:217px;font-size:31px">Every</span>
    <span class="line pink" style="left:141px;width:130px;text-align:center;top:248px;font-size:42px">Day?</span>
  </h2>
  <p class="tag tag--rose" style="left:120px;top:291px;width:164px">Stay Consistent with MB<br>in Your Pocket!</p>
</section>

<!-- Row 3 -->
<section class="post" style="left:310px;top:750px">
  <div class="arch" style="left:30px;top:60px;width:210px;height:310px"></div>
  <div class="photo photo--portrait" role="img" aria-label="Photo of MB smiling with hand on hip" style="left:161px;top:86px;width:123px;height:268px"></div>
  <h2 class="headline">
    <span class="line pink" style="left:20px;top:28px;font-size:34px">The Missing</span>
    <span class="line pink" style="left:20px;top:61px;font-size:53px">Piece</span>
    <span class="line" style="left:20px;top:111px;font-size:52px">Isn't</span>
    <span class="line" style="left:20px;top:163px;font-size:26px">Another</span>
    <span class="line" style="left:20px;top:189px;font-size:52px">Diet</span>
  </h2>
  <p class="tag tag--plum" style="left:21px;top:245px;width:158px">Stay Consistent with MB<br>in Your Pocket!</p>
</section>

<section class="post post--dark" style="left:606px;top:750px">
  <div class="arch" style="left:39px;top:33px;width:206px;height:330px"></div>
  <h2 class="headline">
    <span class="line line--center pink" style="top:53px;font-size:31px">Eat The Food</span>
    <span class="line line--center pink" style="top:89px;font-size:42px">You Love.</span>
    <span class="line line--center light" style="top:131px;font-size:75px">Stay</span>
    <span class="line line--center light" style="top:207px;font-size:30px">Accountable</span>
    <span class="line line--center light" style="top:241px;font-size:39px">Every Day.</span>
  </h2>
  <p class="tag" style="left:0;width:284px;top:286px;text-align:center;font-size:12px;padding:0">Stay Consistent with MB in Your Pocket!</p>
</section>

</body>
</html>
```